Small seafood market and service dock needs a logo and product labels

We need a logo, and product labels, we are a small seafood market and service dock located in Pacific Northwest, Garibaldi Oregon harbor, we provide services such as unloading from boat ,fish cleaning, filleting by owner Norma "The Hook" a local legend , icing, cooking of Dungeness crab on our dock, our small market offers a variety of seafoods , fresh local fish fillets , whole fish as well as live fish , crab, clams, oysters, we are a licensed dealer, we buy from local fishermen, we also fish for our own supply of fresh fish from either of our commercial fishing vessels, Brave Morning or Copper Wren. we offer locally canned Albacore Tuna by the single 8 oz can or by the 24/8oz can case. we desperately need labels as this seasons cans are ready. we offer a variety of flavors , no salt, smoked, garlic, jalapeno ,regular , we hope you can help us The Cove is the name of our store we previously labeled our cans as( Cove Fresh Albacore Tuna) we do have a web page that is partially set up just search google for The Cove.
its painfully obvious we need help with this marketing stuff.

```html
<!DOCTYPE html>
<html lang="en">
<head>
<meta charset="utf-8">
<title>Cove Fresh – Logos and Labels</title>
<link rel="stylesheet" href="https://fonts.googleapis.com/css2?family=Source+Sans+3:wght@400;600&family=Arimo:wght@400&display=swap">
<style>
  :root {
    --ink: #2b2a2c;
    --caption: #8b8b8b;
    --garlic: #e21f2d;
    --smoked: #a5207f;
    --jalapeno: #f3dd0a;
    --nosalt: #0e9e8e;
    --regular: #264f96;
    --paper: #ffffff;
    --frame: #3a3a3a;
  }
  * { box-sizing: border-box; margin: 0; padding: 0; }
  html, body { width: 1023px; height: 1200px; overflow: hidden; background: var(--paper); }
  body { position: relative; font-family: "Source Sans 3", "Myriad Pro", sans-serif; color: var(--ink); }

  .caption { position: absolute; font-family: Arimo, Arial, sans-serif; font-size: 36px; color: var(--caption); transform: translateX(-50%); line-height: 1; }

  .logo-board { position: absolute; top: 217px; width: 432px; height: 232px; border: 1px solid var(--frame); background: var(--paper); }
  .logo-board--one { left: 36px; }
  .logo-board--two { left: 505px; }

  .wordmark { position: absolute; font-weight: 600; color: var(--ink); white-space: nowrap; line-height: 1; }
  .logo-board--one .wordmark { left: 34px; top: 78px; font-size: 74px; }
  .logo-board--one .mark-ring { position: absolute; left: 372px; top: 82px; }
  .logo-board--two .mark-square { position: absolute; left: 20px; top: 79px; width: 111px; height: 72px; background: var(--garlic); }
  .logo-board--two .wordmark { left: 144px; top: 88px; font-size: 50px; text-transform: uppercase; letter-spacing: 1px; }

  .label { position: absolute; width: 306px; height: 271px; border: 1px solid var(--frame); }
  .label--garlic { left: 31px; top: 460px; background: var(--garlic); }
  .label--smoked { left: 358px; top: 460px; background: var(--smoked); }
  .label--jalapeno { left: 686px; top: 460px; background: var(--jalapeno); }
  .label--nosalt { left: 31px; top: 753px; background: var(--nosalt); }
  .label--regular { left: 358px; top: 753px; background: var(--regular); }

  .label__flavor { position: absolute; left: 0; right: 0; top: 14px; text-align: center; color: var(--paper); font-weight: 600; font-size: 50px; line-height: 1; letter-spacing: 0.5px; }
  .label__panel { position: absolute; left: 17px; right: 17px; top: 83px; height: 170px; background: var(--paper); }

  .label__line { position: absolute; left: 5px; font-size: 15px; font-weight: 600; line-height: 20px; white-space: nowrap; }
  .packed-for { top: 8px; left: 8px; }
  .packed-for--inline { top: 17px; font-size: 17px; }
  .packed-by-store { top: 74px; }
  .address { top: 94px; }
  .net-weight { top: 140px; font-size: 13px; font-weight: 400; }

  .brand-chip { position: absolute; display: flex; align-items: center; gap: 8px; }
  .brand-chip__square { width: 72px; height: 48px; }
  .label--garlic .brand-chip { left: 8px; top: 29px; }
  .label--garlic .brand-chip__square { background: var(--garlic); }
  .label--smoked .brand-chip { left: 8px; top: 14px; }
  .label--smoked .brand-chip__square { background: var(--smoked); }
  .brand-chip__name { font-weight: 600; font-size: 31px; text-transform: uppercase; line-height: 1; white-space: nowrap; letter-spacing: 0.5px; }

  .brand-inline { position: absolute; left: 120px; top: 10px; display: flex; align-items: center; gap: 5px; font-weight: 600; font-size: 28px; line-height: 1; white-space: nowrap; }
</style>
</head>
<body>
  <div class="caption" style="left:275px; top:172px;">logo 1</div>
  <div class="caption" style="left:740px; top:172px;">logo 2</div>

  <section class="logo-board logo-board--one">
    <span class="wordmark">Cove Fresh</span>
    <svg class="mark-ring" width="40" height="40" viewBox="0 0 40 40" aria-hidden="true">
      <circle cx="20" cy="20" r="16" fill="none" stroke="var(--garlic)" stroke-width="6"/>
    </svg>
  </section>

  <section class="logo-board logo-board--two">
    <div class="mark-square"></div>
    <span class="wordmark">Cove Fresh</span>
  </section>

  <article class="label label--garlic">
    <h2 class="label__flavor">GARLIC</h2>
    <div class="label__panel">
      <p class="label__line packed-for">Packed for:</p>
      <div class="brand-chip"><span class="brand-chip__square"></span><span class="brand-chip__name">Cove Fresh</span></div>
      <p class="label__line address">118 Harbor Slip,<br>Netarts OR 97143 (503) 555-0142</p>
      <p class="label__line net-weight">Also Net Wt 8 Oz (227g)</p>
    </div>
  </article>

  <article class="label label--smoked">
    <h2 class="label__flavor">SMOKED</h2>
    <div class="label__panel">
      <div class="brand-chip"><span class="brand-chip__square"></span><span class="brand-chip__name">Cove Fresh</span></div>
      <p class="label__line packed-by-store">Packed for The Cove</p>
      <p class="label__line address">118 Harbor Slip,<br>Netarts OR 97143 (503) 555-0142</p>
      <p class="label__line net-weight">Also Net Wt 8 Oz (227g)</p>
    </div>
  </article>

  <article class="label label--jalapeno">
    <h2 class="label__flavor">JALAPENO</h2>
    <div class="label__panel">
      <p class="label__line packed-for--inline">Packed for</p>
      <div class="brand-inline">
        <span>Cove Fresh</span>
        <svg width="20" height="20" viewBox="0 0 20 20" aria-hidden="true"><circle cx="10" cy="10" r="7.5" fill="none" stroke="var(--garlic)" stroke-width="3"/></svg>
      </div>
      <p class="label__line address">118 Harbor Slip,<br>Netarts OR 97143 (503) 555-0142</p>
      <p class="label__line net-weight">Also Net Wt 8 Oz (227g)</p>
    </div>
  </article>

  <div class="caption" style="left:811px; top:745px;">labels</div>

  <article class="label label--nosalt">
    <h2 class="label__flavor">NO SALT</h2>
    <div class="label__panel">
      <p class="label__line packed-by-store">Packed for The Cove</p>
      <p class="label__line address">118 Harbor Slip,<br>Netarts OR 97143 (503) 555-0142</p>
      <p class="label__line net-weight">Also Net Wt 8 Oz (227g)</p>
    </div>
  </article>

  <article class="label label--regular">
    <h2 class="label__flavor">REGULAR</h2>
    <div class="label__panel">
      <p class="label__line packed-by-store">Packed for The Cove</p>
      <p class="label__line address">118 Harbor Slip,<br>Netarts OR 97143 (503) 555-0142</p>
      <p class="label__line net-weight">Also Net Wt 8 Oz (227g)</p>
    </div>
  </article>
</body>
</html>
```